Investment Management Client Email Template

We need an email template to send out monthly returns of our investment strategies to all clients as well as quarterly investment letters. We want to see an elegant somewhat simple design (not overly graphic) that portrays exclusivity, experience, expertise. Nothing playful or too high tech. Our clients are often high net worth middle age or older. We have also won several awards which are included in the attachments along with our logo. We will want to email a letter as the body or a chart. We should have room for a disclaimer at the bottom. The attachments can be used in the design of the graphics.

Target Market(s)

high net worth clientelle

Industry/Entity Type

Financial Planning

Requirements
Must have
• a clean elegant design with the majority of the body being a chart or text as in a letter. use the colors of the logo - blues, grays blacks. Design must look good in outlook or on an iPhone.
• There should be a space for text as the body, a disclaimer at the bottom and an address at the bottom.
Should not have
• Overly graphic. Highlight should be the chart (table) or text. Graphics should make the template look professional but not overly busy.

```html
<!DOCTYPE html>
<html lang="en">
<head>
<meta charset="utf-8">
<title>Keystone Ridge Advisors – Client Letter</title>
<link href="https://fonts.googleapis.com/css2?family=EB+Garamond:ital,wght@0,400;1,700&family=Source+Sans+3:wght@400;600;700&display=swap" rel="stylesheet">
<style>
  :root {
    --navy: #262f86;
    --navy-deep: #1c2366;
    --royal: #3a46a8;
    --link-blue: #4a55b0;
    --ink: #1b1b1b;
    --title-gray: #575757;
    --soft-gray: #8c8c8c;
    --mid-gray: #a7a8aa;
    --panel-gray: #d3d4d6;
    --panel-light: #ececec;
    --footer-gray: #6d6e71;
    --paper: #ffffff;
  }
  * { margin: 0; padding: 0; box-sizing: border-box; }
  html, body { width: 866px; height: 1200px; overflow: hidden; background: var(--paper); }
  .page { position: relative; width: 866px; height: 1200px; overflow: hidden; background: var(--paper); font-family: "Source Sans 3", Arial, sans-serif; }

  .top-bar { position: absolute; left: 0; top: 0; width: 866px; height: 30px; background: linear-gradient(90deg, var(--royal), var(--navy-deep)); }
  .header-art { position: absolute; left: 0; top: 30px; width: 866px; height: 210px; }
  .issue-date { position: absolute; left: 704px; top: 66px; font-size: 19px; font-weight: 700; color: #d8d9db; letter-spacing: .2px; }
  .issue-date span { font-weight: 400; }

  .brand { position: absolute; left: 104px; top: 92px; display: flex; align-items: center; gap: 12px; }
  .brand-mark { width: 48px; height: 48px; border-radius: 50%; background: var(--navy); }
  .brand-name { font-size: 30px; font-weight: 600; color: var(--navy); line-height: 1.05; }

  .letter-title { position: absolute; left: 117px; top: 222px; font-size: 40px; font-weight: 400; color: var(--title-gray); }
  .letter-body { position: absolute; left: 123px; top: 290px; width: 640px; font-family: "EB Garamond", Georgia, serif; font-size: 15.6px; line-height: 19.5px; color: var(--ink); text-align: justify; }
  .letter-body p { margin-bottom: 19.5px; }
  .signature { position: absolute; left: 130px; top: 692px; font-family: "EB Garamond", Georgia, serif; font-style: italic; font-weight: 700; font-size: 15.6px; color: var(--ink); }

  .lower-panel { position: absolute; left: 0; top: 823px; width: 490px; height: 377px; background: var(--panel-gray); }
  .contact-panel { position: absolute; left: 490px; top: 870px; width: 376px; height: 330px; background: var(--panel-light); }
  .awards-band { position: absolute; left: 0; top: 745px; width: 866px; height: 145px; }

  .note-title { position: absolute; left: 69px; top: 879px; font-size: 24px; color: #7a7a7a; }
  .note-text { position: absolute; left: 69px; top: 920px; width: 350px; font-size: 13.6px; line-height: 23px; color: var(--soft-gray); }

  .contact { position: absolute; left: 561px; top: 905px; font-size: 13.2px; line-height: 17.5px; color: var(--soft-gray); }
  .contact h3 { font-size: 13.2px; font-weight: 700; color: var(--link-blue); }
  .contact .block { margin-bottom: 17.5px; }

  .footer { position: absolute; left: 0; top: 1158px; width: 866px; height: 42px; }
  .footer-url { position: absolute; left: 561px; top: 1170px; font-size: 13px; font-weight: 700; color: #d6d6d8; }
</style>
</head>
<body>
<div class="page">
  <div class="top-bar"></div>

  <svg class="header-art" viewBox="0 30 866 210" width="866" height="210">
    <defs>
      <linearGradient id="skyline" x1="0" y1="0" x2="0" y2="1">
        <stop offset="0" stop-color="#9cc6ec"/>
        <stop offset=".55" stop-color="#4f8fcf"/>
        <stop offset="1" stop-color="#2f5f9a"/>
      </linearGradient>
    </defs>
    <polygon points="547,30 866,30 866,121 601,121" fill="var(--mid-gray)"/>
    <polygon points="461,121 866,121 866,238 524,238" fill="url(#skyline)" role="img" aria-label="Photo of glass office towers against a blue sky"/>
  </svg>
  <div class="issue-date">january <span>12</span></div>

  <div class="brand">
    <div class="brand-mark"></div>
    <div class="brand-name">Keystone Ridge Advisors</div>
  </div>

  <h1 class="letter-title">Title here</h1>
  <div class="letter-body">
    <p>"Lorem ipsum dolor sit amet, consectetur adipiscing elit, sed do eiusmod tempor incididunt ut labore et dolore magna aliqua. Ut enim ad minim veniam, quis nostrud exercitation ullamco laboris nisi ut aliquip ex ea commodo consequat. Duis aute irure dolor in reprehenderit in voluptate velit esse cillum dolore eu fugiat nulla pariatur. Excepteur sint occaecat cupidatat non proident, sunt in culpa qui officia deserunt mollit anim id est laborum."</p>
    <p>"Lorem ipsum dolor sit amet, consectetur adipiscing elit, sed do eiusmod tempor incididunt ut labore et dolore magna aliqua. Ut enim ad minim veniam, quis nostrud exercitation ullamco laboris nisi ut aliquip ex ea commodo consequat. Duis aute irure dolor in reprehenderit in voluptate velit esse cillum dolore eu fugiat nulla pariatur. Excepteur sint occaecat cupidatat non proident, sunt in culpa qui officia deserunt mollit anim id est laborum."</p>
    <p>"Lorem ipsum dolor sit amet, consectetur adipiscing elit, sed do eiusmod tempor incididunt ut labore et dolore magna aliqua. Ut enim ad minim veniam, quis nostrud exercitation ullamco laboris nisi ut aliquip ex ea commodo consequat. Duis aute irure dolor in reprehenderit in voluptate velit esse cillum dolore eu fugiat nulla pariatur. Excepteur sint occaecat cupidatat non proident, sunt in culpa qui officia deserunt mollit anim id est laborum."</p>
  </div>
  <div class="signature">Lorem ipsum</div>

  <div class="lower-panel"></div>
  <div class="contact-panel"></div>

  <svg class="awards-band" viewBox="0 745 866 145" width="866" height="145">
    <defs>
      <linearGradient id="band" x1="0" y1="0" x2="1" y2="0">
        <stop offset="0" stop-color="#2d3896"/>
        <stop offset="1" stop-color="#252d82"/>
      </linearGradient>
      <radialGradient id="seal" cx=".4" cy=".35" r=".7">
        <stop offset="0" stop-color="#f6dc86"/>
        <stop offset="1" stop-color="#c89a2c"/>
      </radialGradient>
    </defs>
    <polygon points="290,754 866,754 866,884 358,884" fill="#000" opacity=".18"/>
    <polygon points="285,750 866,750 866,877 352,877" fill="url(#band)"/>
    <rect x="361" y="776" width="107" height="61" fill="#ffffff"/>
    <circle cx="550" cy="810" r="41" fill="url(#seal)"/>
    <rect x="635" y="768" width="58" height="80" fill="#1e1e22" stroke="#c8c8c8" stroke-width="2"/>
    <rect x="755" y="767" width="58" height="80" fill="#1e1e22" stroke="#c8c8c8" stroke-width="2"/>
  </svg>

  <h2 class="note-title">Title here</h2>
  <p class="note-text">"Lorem ipsum dolor sit amet, consectetur adipiscing elit, sed do eiusmod tempor incididunt ut labore et dolore magna aliqua. Ut enim ad minim veniam, quis nostrud exercitation ullamco laboris nisi ut aliquip ex ea commodo consequat. Duis aute irure dolor in reprehenderit in voluptate velit esse cillum dolore eu fugiat nulla pariatur. Excepteur sint occaecat cupidatat non proident, sunt in culpa qui officia deserunt mollit anim id est laborum."</p>

  <div class="contact">
    <div class="block">
      <h3>Keystone Ridge Advisors<br>Office Location</h3>
      2200 Larkspur Ave STE 310<br>Fairhaven, TX 75021
    </div>
    <div class="block">
      <h3>Mailing Address</h3>
      880 Elmridge Blvd STE 12 #207<br>Fairhaven, TX 75024
    </div>
    <div class="block">
      P: 555-210-4800<br>F: 555-310-7722<br>E: hello@keystoneridge.example
    </div>
  </div>

  <svg class="footer" viewBox="0 1158 866 42" width="866" height="42">
    <polygon points="389,1158 866,1158 866,1200 412,1200" fill="var(--footer-gray)"/>
  </svg>
  <div class="footer-url">www.keystoneridge.example</div>
</div>
</body>
</html>
```